依頼詳細
新規の取引の際にもホームページや会社案内を見て頂き、安心してお取引いただけるようになればと考えております。

日々お客様からご依頼いただき、買い取らせていただいている様々な金属を具体的にホームページに掲載し、こんなものも買い取ってもらえるんだということをお客様に知っていただければと考えております。

個人から個人事業主、法人のお客様の開拓と、栃木県内だけでなくより広範囲のお客様の開拓も行っていきます。

画像等は、有料素材サイトなどからのご提案もお願いいたします。
会社のロゴは、添付のロゴ写真を参考にして下さい。(株)ではなく株式会社にして下さい。フォントは同じようなものでお願いします。
サイトURL
ページ数
1ページ
希望イメージ
シンプル 複雑
単色 カラフル
暗い 明るい
日常 高級
遊び心 厳粛
未来的 伝統的
女性的 男性的
希望する色
青系、ロゴの色をメインカラーにして下さい。
納品ファイル
• 高解像度JPG (.jpg)
• イラストレーター形式 (.ai)
• フォトショップ形式 (.psd)
補足説明
レスポンシブデザインにてご提案をお願い致します。
スマートフォンのデザインもご提示いただければと思います。
お世話になっております。もう提案をいただきたいと思います。
よろしくお願いいたします。
■ 選んだ理由

お客様が大変悩まれておりましたが、素晴らしいデザインといっていただけました。ありがとうございました。今後修正等があるかと思いますが引き続きよろしくお願いします。

■ 提案者全員のお礼・コメント

たくさんのデザインありがとうございました。
お客様も大変悩まれておりました。
今後もデザインコンペを行ってまいりますのでよろしくお願いいたします。

```html
<!DOCTYPE html>
<html lang="ja">
<head>
<meta charset="utf-8">
<title>株式会社 丸泉 | 金属・非鉄金属買取</title>
<link href="https://fonts.googleapis.com/css2?family=Noto+Sans+JP:wght@400;500;700;900&display=swap" rel="stylesheet">
<style>
:root{
  --navy:#1d2f7a;
  --blue:#2a48a8;
  --ink:#333a4a;
  --muted:#777d8a;
  --line:#c9ccd6;
  --nav:#5b5f6a;
  --foot:#6b6f78;
  --copy:#3e4350;
  --red:#c8232c;
  --copper1:#b5562c;
  --copper2:#e3a06b;
  --steel1:#8c939c;
  --steel2:#e7ebef;
}
*{margin:0;padding:0;box-sizing:border-box}
html,body{width:1200px;height:3644px;overflow:hidden}
body{font-family:"Noto Sans JP",sans-serif;color:var(--ink);background:#fff;position:relative}
.abs{position:absolute}
.topline{top:0;left:0;width:1200px;height:22px;font-size:11px;color:var(--muted);padding:5px 24px;letter-spacing:.5px}
.header{top:22px;left:0;width:1200px;height:98px}
.brand{left:24px;top:16px;display:flex;align-items:center;gap:12px}
.brand-dot{width:54px;height:54px;border-radius:50%;background:var(--navy)}
.brand-name{font-size:30px;font-weight:700;color:var(--navy);letter-spacing:2px}
.contact{right:40px;top:14px;text-align:right}
.contact small{display:block;font-size:13px;color:var(--muted)}
.contact .tel{display:flex;align-items:center;gap:10px;font-size:40px;font-weight:500;color:var(--navy);letter-spacing:2px;line-height:1.1}
.nav{top:120px;left:0;width:1200px;height:30px;background:var(--nav);display:flex;padding-left:24px}
.nav a{width:128px;text-align:center;color:#fff;font-size:13px;line-height:30px;text-decoration:none;border-right:1px solid rgba(255,255,255,.35)}
.nav a.on{background:var(--blue)}
.hero{top:150px;left:0;width:1200px;height:410px;background:linear-gradient(160deg,#5c636c,#c9cfd5 35%,#7c848d 60%,#dfe3e7)}
.hero-band{top:60px;left:0;width:1200px;height:86px;background:linear-gradient(90deg,rgba(20,36,90,.85),rgba(40,70,150,.55) 60%,rgba(40,70,150,0))}
.hero-title{top:68px;left:60px;font-size:60px;font-weight:900;color:#fff;font-style:italic;letter-spacing:4px}
.hero-sub{top:250px;right:40px;font-size:46px;font-weight:900;color:#fff;font-style:italic;letter-spacing:4px;text-shadow:0 2px 6px rgba(0,0,0,.5)}
.h2{font-size:34px;font-weight:500;color:var(--navy);letter-spacing:2px}
.h2-line{height:2px;background:var(--navy)}
.txt{font-size:15px;line-height:1.9;color:var(--ink)}
.btn{border:1px solid var(--navy);color:var(--navy);font-size:13px;text-align:center;line-height:26px;background:#fff}
.photo{border-radius:2px}
.card-label{font-size:13px;color:var(--ink)}
.price{font-size:20px;color:var(--muted);letter-spacing:2px}
.qa p{font-size:17px;line-height:1.6;color:var(--ink)}
.qa .q{color:var(--red)}
.qa .a{color:var(--blue)}
.qa .row{border-bottom:1px solid var(--line);padding:6px 0 10px;margin-bottom:12px}
.news-row{display:flex;border-bottom:1px solid var(--line);font-size:15px;color:var(--ink);height:42px;align-items:center}
.news-row span:first-child{width:220px;padding-left:20px}
.footnav{top:3544px;left:0;width:1200px;height:38px;background:var(--foot);display:flex;justify-content:center}
.footnav a{color:#fff;font-size:13px;text-decoration:none;line-height:38px;width:132px;text-align:center;border-right:1px solid rgba(255,255,255,.3)}
.copy{top:3582px;left:0;width:1200px;height:62px;background:var(--copy);color:#fff;text-align:center;font-size:14px;line-height:62px;letter-spacing:1px}
</style>
</head>
<body>
<div class="abs topline">金属・非鉄金属の買取なら株式会社 丸泉へ。個人・法人問わず県内外からのご依頼に丁寧に対応いたします。</div>

<header class="abs header">
  <div class="abs brand"><span class="brand-dot"></span><span class="brand-name">株式会社 丸泉</span></div>
  <div class="abs contact">
    <small>お気軽にお電話下さい</small>
    <div class="tel">
      <svg width="30" height="30" viewBox="0 0 24 24"><path fill="#1d2f7a" d="M6.6 10.8a15.1 15.1 0 0 0 6.6 6.6l2.2-2.2c.3-.3.7-.4 1-.2 1.1.4 2.3.6 3.6.6.6 0 1 .4 1 1V20c0 .6-.4 1-1 1A17 17 0 0 1 3 4c0-.6.4-1 1-1h3.5c.6 0 1 .4 1 1 0 1.3.2 2.5.6 3.6.1.3 0 .7-.2 1z"/></svg>
      0120-45-6789
    </div>
  </div>
</header>

<nav class="abs nav">
  <a class="on">HOME</a><a>買取について</a><a>買取の流れ</a><a>買取実績</a><a>会社概要</a><a>お問い合わせ</a>
</nav>

<section class="abs hero" role="img" aria-label="積み重なった金属パイプの写真"></section>
<div class="abs hero-band"></div>
<div class="abs hero-title" style="top:218px">迅速対応、完璧な仕事</div>
<div class="abs hero-sub" style="top:390px">金属、非鉄金属買取致します</div>

<!-- こだわり -->
<div class="abs photo" role="img" aria-label="金属パイプの断面の写真" style="top:600px;left:640px;width:560px;height:450px;background:linear-gradient(90deg,#fff,#dfe3e8 35%,#b9c0c8)"></div>
<div class="abs h2" style="top:612px;left:132px">丸泉のこだわり</div>
<div class="abs h2-line" style="top:664px;left:132px;width:440px"></div>
<p class="abs txt" style="top:684px;left:132px;width:460px">私たちは一つひとつの金属を丁寧に見極め、適正な価格で買い取ることを大切にしています。お客様に安心してご依頼いただけるよう、査定の内容をわかりやすくご説明いたします。鉄くずから非鉄金属まで幅広く対応し、少量のお持ち込みから大量の回収まで柔軟にお受けいたします。地域に根ざした企業として、迅速で誠実な仕事をお約束します。</p>

<!-- 買取について -->
<div class="abs photo" role="img" aria-label="金属を運ぶトラックの写真" style="top:1070px;left:0;width:640px;height:370px;background:linear-gradient(120deg,#c9b21a,#8a8f98 40%,#c7ccd3 75%,#fff)"></div>
<div class="abs h2" style="top:1116px;left:760px">買取について</div>
<div class="abs h2-line" style="top:1168px;left:620px;width:580px"></div>
<p class="abs txt" style="top:1194px;left:740px;width:420px">銅・真鍮・アルミ・ステンレスなど、様々な金属を買い取っております。個人のお客様から法人様まで、県内外を問わずお気軽にご相談ください。お見積もりは無料です。</p>
<div class="abs btn" style="top:1320px;left:980px;width:170px">詳しくはこちら ▶</div>

<!-- 買取実績 -->
<div class="abs" role="img" aria-label="スクラップ置き場の写真" style="top:1450px;left:0;width:1200px;height:750px;background:linear-gradient(180deg,#fff,#eef0f3 50%,#d3d8de 85%,#fff)"></div>
<div class="abs h2" style="top:1504px;left:0;width:1200px;text-align:center">買取実績</div>
<div class="abs h2-line" style="top:1556px;left:470px;width:260px"></div>

<div class="abs photo" role="img" aria-label="銅線スクラップの写真" style="top:1620px;left:270px;width:300px;height:80px;background:linear-gradient(135deg,var(--copper1),var(--copper2))"></div>
<div class="abs card-label" style="top:1706px;left:270px">静岡県 M様</div>
<div class="abs price" style="top:1720px;left:420px">○○○○円</div>

<div class="abs photo" role="img" aria-label="銅管スクラップの写真" style="top:1620px;left:630px;width:300px;height:80px;background:linear-gradient(135deg,#a64b24,#d98c57)"></div>
<div class="abs card-label" style="top:1706px;left:630px">群馬県 K様</div>
<div class="abs price" style="top:1720px;left:780px">○○○○円</div>

<div class="abs photo" role="img" aria-label="銅線の束の写真" style="top:1830px;left:270px;width:300px;height:80px;background:linear-gradient(135deg,#c06a3a,#e8b07f)"></div>
<div class="abs card-label" style="top:1916px;left:270px">広島県 O様</div>
<div class="abs price" style="top:1930px;left:420px">○○○○円</div>

<div class="abs photo" role="img" aria-label="真鍮スクラップの写真" style="top:1830px;left:630px;width:300px;height:80px;background:linear-gradient(135deg,#8a6a3a,#cfb07a)"></div>
<div class="abs card-label" style="top:1916px;left:630px">埼玉県 F様</div>
<div class="abs price" style="top:1930px;left:780px">○○○○円</div>

<div class="abs btn" style="top:2034px;left:480px;width:240px">その他の買取事例はこちら ▶</div>

<!-- よくある質問 -->
<div class="abs h2" style="top:2250px;left:132px">買取のよくある質問</div>
<div class="abs h2-line" style="top:2302px;left:132px;width:560px"></div>
<div class="abs qa" style="top:2330px;left:132px;width:460px">
  <div class="row"><p class="q">Q.○○○○○○○○○○？</p><p class="a">A.■■■■■</p></div>
  <div class="row"><p class="q">Q.○○○○○○○○○○？</p><p class="a">A.■■■■■</p></div>
  <div class="row"><p class="q">Q.○○○○○○○○○○？</p><p class="a">A.■■■■■</p></div>
  <div class="row"><p class="q">Q.○○○○○○○○○○？</p><p class="a">A.■■■■■</p></div>
</div>
<div class="abs" role="img" aria-label="ヘッドセットを付けた受付担当者の写真" style="top:2300px;left:800px;width:240px;height:430px;background:linear-gradient(180deg,#eceef1,#3a3d44 60%,#2a2c31)"></div>

<!-- 買取可能な金属類 -->
<div class="abs h2" style="top:2780px;left:0;width:1200px;text-align:center">買取可能な金属類</div>
<div class="abs h2-line" style="top:2832px;left:430px;width:340px"></div>
<div class="abs" role="img" aria-label="金属置き場の写真" style="top:2850px;left:0;width:1200px;height:260px;background:linear-gradient(180deg,#fff,#e4e7eb 50%,#fff)"></div>
<div class="abs photo" role="img" aria-label="金属の写真" style="top:2876px;left:134px;width:150px;height:80px;background:linear-gradient(135deg,var(--copper1),var(--copper2))"></div>
<div class="abs photo" role="img" aria-label="金属の写真" style="top:2876px;left:320px;width:150px;height:80px;background:linear-gradient(135deg,#a64b24,#d98c57)"></div>
<div class="abs photo" role="img" aria-label="金属の写真" style="top:2876px;left:506px;width:150px;height:80px;background:linear-gradient(135deg,#c06a3a,#e8b07f)"></div>
<div class="abs photo" role="img" aria-label="金属の写真" style="top:2876px;left:692px;width:150px;height:80px;background:linear-gradient(135deg,#b5562c,#e09a62)"></div>
<div class="abs photo" role="img" aria-label="金属の写真" style="top:2876px;left:878px;width:150px;height:80px;background:linear-gradient(135deg,#a9532a,#dc9460)"></div>
<div class="abs card-label" style="top:2966px;left:134px;width:150px;text-align:center">金属の名前</div>
<div class="abs card-label" style="top:2966px;left:320px;width:150px;text-align:center">金属の名前</div>
<div class="abs card-label" style="top:2966px;left:506px;width:150px;text-align:center">金属の名前</div>
<div class="abs card-label" style="top:2966px;left:692px;width:150px;text-align:center">金属の名前</div>
<div class="abs card-label" style="top:2966px;left:878px;width:150px;text-align:center">金属の名前</div>
<div class="abs btn" style="top:3068px;left:500px;width:200px">詳しくはこちら ▶</div>

<!-- 新着情報 -->
<div class="abs h2" style="top:3196px;left:0;width:1200px;text-align:center">新着情報</div>
<div class="abs h2-line" style="top:3248px;left:520px;width:160px"></div>
<div class="abs" style="top:3290px;left:270px;width:660px;border-top:1px solid var(--line)">
  <div class="news-row"><span>2017.7.28</span><span>ホームページ開設</span></div>
  <div class="news-row"><span>2017.7.28</span><span>ホームページ開設</span></div>
  <div class="news-row"><span>2017.7.28</span><span>ホームページ開設</span></div>
</div>

<footer>
  <nav class="abs footnav"><a>HOME</a><a>買取について</a><a>買取の流れ</a><a>買取実績</a><a>会社概要</a><a>お問い合わせ</a></nav>
  <div class="abs copy">copyright(c) 株式会社 丸泉　栃木県みどり市</div>
</footer>
</body>
</html>
```